Financial Advisor Graphic to Explain Proprietary and Differentiating Investment Strategy

We need a graphic that visualizes how we build a portfolio based on factors of the underlying companies. We use 8 main factors to objectively build an investment porftolio. Our colors are blues, greys (see www.pltvexgroup.com). We are thinking either a venn diagram approach or an atom approach with the factors around the middle "Core Portfolio". This is what differentiates us from everyone in the industry. This will be the key to all of our marketing

Target Market(s)

High net worth investors

Industry/Entity Type

Financial Service

Font styles to use
Serif

Requirements
Must have
• Graphic must be elegant. It is for the financial industry. It should include the following factors (in no order) to build a "Core Portfolio"
• -Counter Cyclical Industries
• -Industry Rate of Recovery
• -Price To Book
• -Absolute Risk
• -Market Capitalization
• -Liquidity
• -Dividend Yield
• -Buy Back Yield
Nice to have
• We are thinking an atom approach or a venn diagram but we are open to new ideas. It must portray the idea that we OBJECTIVELY apply these factors to stock selection to build a core portfolio for our investors. For color pallets see www.pltvexgroup.com It can go beyond the greys and blues but should not be too loud or playful. It can be high tech as long as it portrays seriousness of the financial markets
Should not have
• Can not be playful.

```html
<!DOCTYPE html>
<html lang="en">
<head>
<meta charset="utf-8">
<title>Core Portfolio Factors</title>
<link rel="stylesheet" href="https://fonts.googleapis.com/css2?family=Poppins:wght@500;600&display=swap">
<style>
  :root {
    --bg: #ffffff;
    --ink: #262626;
    --brand: #2a2aa8;
    --node-light: #7a78dc;
    --node-dark: #4a46c2;
    --connector: #cfcfcf;
    --dot-dark: #8c8c8c;
    --dot-light: #c4c4c4;
    --icon: #ffffff;
  }
  html, body {
    margin: 0;
    padding: 0;
    width: 1200px;
    height: 1200px;
    overflow: hidden;
    background: var(--bg);
  }
  .canvas {
    position: relative;
    width: 1200px;
    height: 1200px;
    font-family: "Poppins", sans-serif;
    color: var(--ink);
  }
  .factor-map {
    position: absolute;
    inset: 0;
    width: 1200px;
    height: 1200px;
  }
  .brand {
    position: absolute;
    left: 30px;
    top: 36px;
    display: flex;
    align-items: center;
    gap: 16px;
  }
  .brand-mark {
    width: 54px;
    height: 54px;
    border-radius: 50%;
    background: var(--brand);
  }
  .brand-name {
    font-family: "Poppins", sans-serif;
    font-weight: 500;
    font-size: 28px;
    color: var(--brand);
    letter-spacing: 0.2px;
  }
  .factor-label {
    position: absolute;
    margin: 0;
    font-weight: 600;
    font-size: 27px;
    line-height: 35px;
    color: var(--ink);
    white-space: nowrap;
  }
  .label-absolute-risk { left: 680px; top: 231px; }
  .label-market-cap    { left: 982px; top: 369px; }
  .label-price-book    { left: 70px;  top: 414px; }
  .label-industry-rate { left: 94px;  top: 552px; }
  .label-buy-back      { left: 40px;  top: 704px; }
  .label-liquidity     { left: 896px; top: 532px; }
  .label-dividend      { left: 1016px; top: 621px; }
  .label-counter       { left: 884px; top: 753px; }
  .core-title {
    position: absolute;
    left: 477px;
    top: 898px;
    width: 240px;
    margin: 0;
    text-align: center;
    font-weight: 600;
    font-size: 42px;
    line-height: 53px;
    color: #ffffff;
  }
</style>
</head>
<body>
<div class="canvas">
  <svg class="factor-map" viewBox="0 0 1500 1500" aria-hidden="true">
    <defs>
      <linearGradient id="nodeFill" x1="0" y1="0" x2="1" y2="1">
        <stop offset="0" stop-color="#8a88e2"/>
        <stop offset="1" stop-color="#4a46c2"/>
      </linearGradient>
      <filter id="nodeShadow" x="-40%" y="-40%" width="180%" height="180%">
        <feDropShadow dx="0" dy="10" stdDeviation="10" flood-color="#5b58d0" flood-opacity="0.35"/>
      </filter>
    </defs>

    <g class="connectors" fill="none" stroke="#cfcfcf" stroke-width="3">
      <path d="M736 375 V1060"/>
      <path d="M487 538 H675 Q701 538 701 564 V1060"/>
      <path d="M520 733 H645 Q671 733 671 759 V1070"/>
      <path d="M375 918 H619 Q645 918 645 944 V1085"/>
      <path d="M1060 505 H796 Q770 505 770 531 V1060"/>
      <path d="M955 688 H827 Q801 688 801 714 V1060"/>
      <path d="M1108 825 H853 Q827 825 827 851 V1070"/>
      <path d="M932 986 H874 Q848 986 848 1012 V1085"/>
    </g>

    <g class="connector-dots">
      <circle cx="736" cy="453" r="11" fill="#8c8c8c"/>
      <circle cx="736" cy="719" r="11" fill="#c4c4c4"/>
      <circle cx="571" cy="539" r="11" fill="#c4c4c4"/>
      <circle cx="701" cy="840" r="11" fill="#c4c4c4"/>
      <circle cx="596" cy="733" r="11" fill="#c4c4c4"/>
      <circle cx="671" cy="935" r="11" fill="#c4c4c4"/>
      <circle cx="474" cy="918" r="11" fill="#8c8c8c"/>
      <circle cx="645" cy="1010" r="11" fill="#c4c4c4"/>
      <circle cx="855" cy="505" r="11" fill="#8c8c8c"/>
      <circle cx="770" cy="860" r="11" fill="#c4c4c4"/>
      <circle cx="885" cy="688" r="11" fill="#8c8c8c"/>
      <circle cx="801" cy="924" r="11" fill="#c4c4c4"/>
      <circle cx="1010" cy="825" r="11" fill="#8c8c8c"/>
      <circle cx="827" cy="980" r="11" fill="#c4c4c4"/>
      <circle cx="876" cy="990" r="11" fill="#8c8c8c"/>
    </g>

    <g class="factor-nodes" fill="url(#nodeFill)" filter="url(#nodeShadow)">
      <circle cx="740" cy="310" r="65"/>
      <circle cx="422" cy="538" r="65"/>
      <circle cx="455" cy="727" r="65"/>
      <circle cx="310" cy="918" r="65"/>
      <circle cx="1125" cy="497" r="65"/>
      <circle cx="1018" cy="686" r="65"/>
      <circle cx="1173" cy="825" r="65"/>
      <circle cx="996" cy="985" r="65"/>
      <circle class="core-node" cx="746" cy="1193" r="150"/>
    </g>

    <g class="factor-icons" fill="none" stroke="#ffffff" stroke-width="5" stroke-linecap="round" stroke-linejoin="round">
      <!-- absolute risk: warning triangle with dollar -->
      <path d="M740 272 L776 334 H704 Z" fill="#ffffff" stroke="none"/>
      <text x="740" y="327" text-anchor="middle" font-family="Poppins, sans-serif" font-weight="600" font-size="34" fill="#5552c8" stroke="none">$</text>
      <!-- price to book: book -->
      <rect x="398" y="508" width="48" height="60" rx="3"/>
      <path d="M406 508 V568"/>
      <path d="M424 508 V526 L430 521 L436 526 V508"/>
      <text x="418" y="560" text-anchor="middle" font-family="Poppins, sans-serif" font-weight="600" font-size="22" fill="#ffffff" stroke="none">$</text>
      <!-- industry rate of recovery: bars -->
      <rect x="424" y="744" width="12" height="12" fill="#ffffff" stroke="none"/>
      <rect x="442" y="736" width="12" height="20" fill="#ffffff" stroke="none"/>
      <rect x="470" y="724" width="12" height="32" fill="#ffffff" stroke="none"/>
      <path d="M418 760 H490"/>
      <text x="476" y="718" text-anchor="middle" font-family="Poppins, sans-serif" font-weight="600" font-size="30" fill="#ffffff" stroke="none">$</text>
      <!-- buy back yield: gauge -->
      <path d="M296 893 H324 L340 918 L324 943 H296 L280 918 Z"/>
      <circle cx="310" cy="918" r="13"/>
      <path d="M310 918 L318 909"/>
      <!-- market capitalization: hand with coin -->
      <circle cx="1133" cy="482" r="13"/>
      <path d="M1096 516 H1115 Q1135 518 1150 510 L1162 503"/>
      <path d="M1096 508 H1124"/>
      <!-- liquidity: droplet -->
      <path d="M1018 646 Q1040 676 1040 690 A22 22 0 0 1 996 690 Q996 676 1018 646 Z"/>
      <text x="1018" y="700" text-anchor="middle" font-family="Poppins, sans-serif" font-weight="600" font-size="22" fill="#ffffff" stroke="none">$</text>
      <!-- dividend yield: bag with percent -->
      <path d="M1160 812 Q1148 830 1150 846 Q1152 856 1173 856 Q1194 856 1196 846 Q1198 830 1186 812 Z"/>
      <path d="M1162 800 H1184"/>
      <text x="1173" y="848" text-anchor="middle" font-family="Poppins, sans-serif" font-weight="600" font-size="20" fill="#ffffff" stroke="none">%</text>
      <!-- counter cyclical industries: gear with cycle -->
      <circle cx="996" cy="985" r="26"/>
      <circle cx="996" cy="985" r="11"/>
      <path d="M996 952 V959 M996 1011 V1018 M963 985 H970 M1022 985 H1029 M973 962 L978 967 M1014 1003 L1019 1008 M1019 962 L1014 967 M978 1003 L973 1008"/>
    </g>
  </svg>

  <div class="brand">
    <span class="brand-mark"></span>
    <span class="brand-name">Norvale Capital Research</span>
  </div>

  <p class="factor-label label-absolute-risk">Absolute Risk</p>
  <p class="factor-label label-market-cap">Market<br>Capitalization</p>
  <p class="factor-label label-price-book">Price To Book</p>
  <p class="factor-label label-industry-rate">Industry Rate<br>of Recovery</p>
  <p class="factor-label label-buy-back">Buy Back<br>Yield</p>
  <p class="factor-label label-liquidity">Liquidity</p>
  <p class="factor-label label-dividend">Dividend<br>Yield</p>
  <p class="factor-label label-counter">Counter Cyclical<br>Industries</p>

  <h1 class="core-title">Core<br>Portfolio</h1>
</div>
</body>
</html>
```